Redesign specialty cleaning services business brochure

I need a brochure re-designed and updated to reflect packages we sell for starting your own specialty cleaning business. We are a specialty cleaning company that has been in business for over 35 years and our company literature needs an update.The brochure needs to be a downloadable file as well as print-ready.The download will go on 2 of our websites https://dovrantco.com/ and http://tarvelbrookpolishinstitute.com/. I will attach the brochure that needs to be redesigned. They have not been updated for several years. I have new images to add to the updated brochure.
Colors
Designer to choose colors to be used in the design.
Look and feel
Each slider illustrates characteristics of the customer's brand and the style your logo design should communicate.

```html
<!DOCTYPE html>
<html lang="en">
<head>
<meta charset="utf-8">
<title>Window Cleaning Package Brochure</title>
<link rel="stylesheet" href="https://fonts.googleapis.com/css2?family=Questrial&family=Roboto+Condensed:wght@400;700&display=swap">
<style>
:root{
  --green:#1f9a3e;
  --green-text:#1d8a3a;
  --grey-btn:#5d5e60;
  --footer:#4f5052;
  --ink:#3a3a3a;
  --soft:#f1f1f1;
  --grid:#e4e4e4;
  --orange:#f26a1b;
  --white:#ffffff;
}
*{box-sizing:border-box;margin:0;padding:0}
html,body{width:744px;height:1200px;overflow:hidden;background:var(--white)}
body{font-family:"Questrial",sans-serif;color:var(--ink);position:relative}
.spread{position:absolute;left:22px;width:700px;height:496px;overflow:hidden;box-shadow:0 2px 8px rgba(0,0,0,.18)}
.spread--krv{top:60px;background:var(--white)}
.spread--lmt{top:622px;background-color:var(--soft);
  background-image:linear-gradient(var(--grid) 1px,transparent 1px),linear-gradient(90deg,var(--grid) 1px,transparent 1px);
  background-size:42px 42px}
.abs{position:absolute}
.headline{color:var(--green-text);font-size:11.5px;line-height:1.2}
.price-bar{background:var(--green);color:var(--white);display:flex;align-items:center;gap:8px;padding:0 8px 0 18px}
.price-bar small{font-size:8.5px;line-height:1.1}
.price-bar strong{font-family:"Roboto Condensed",sans-serif;font-size:19px;font-weight:700}
.note{font-size:9px}
.lead{font-size:7.5px;font-weight:bold;letter-spacing:.2px}
.tag{border-radius:4px;color:var(--white);font-size:8px;line-height:1.15;padding:4px 6px;width:88px;min-height:22px;display:flex;align-items:center}
.tag--green{background:var(--green)}
.tag--grey{background:var(--grey-btn);justify-content:center;text-align:center}
.bullets{list-style:none;font-size:6.8px;line-height:12px;color:#555}
.bullets li::before{content:"+";color:var(--green);margin-right:4px;font-weight:bold}
.footer{left:0;top:443px;width:700px;height:53px;background:var(--footer);color:var(--white);font-size:8.5px;z-index:1}
.contact{font-size:7px;line-height:10px;display:flex;gap:4px}
.contact svg{flex:none;margin-top:1px}
.task{font-size:13px;line-height:16px;color:#444}
.package-title{font-size:17px;color:#555;text-align:center;z-index:2}
.package-bar{background:var(--green);color:var(--white);font-size:14px;text-align:center;line-height:24px;border:2px solid var(--white);z-index:2}
.url{font-size:10px;color:var(--white)}
.brand{font-family:"Questrial",sans-serif;font-size:11px;color:#222;display:flex;align-items:center;gap:4px}
.brand i{display:block;width:8px;height:8px;background:#222}
.title-bar{background:var(--green);color:var(--white);font-size:14px;line-height:24px;text-align:center;border:2px solid var(--white);border-radius:3px}
.photo-circle{border-radius:50%;border:4px solid var(--white);box-shadow:0 1px 4px rgba(0,0,0,.25)}
.site{font-size:8px;color:var(--green-text)}
.cloud{left:358px;top:36px;width:336px;height:440px}
</style>
</head>
<body>

<section class="spread spread--krv">
  <svg class="abs" style="left:0;top:0" width="700" height="496" viewBox="0 0 700 496">
    <defs>
      <linearGradient id="crew" x1="0" y1="0" x2="1" y2="1">
        <stop offset="0" stop-color="#8a8f96"/><stop offset=".5" stop-color="#5b6470"/><stop offset="1" stop-color="#a9b0b7"/>
      </linearGradient>
      <linearGradient id="pole" x1="0" y1="0" x2="0" y2="1">
        <stop offset="0" stop-color="#b9c6d2"/><stop offset="1" stop-color="#4c5a6b"/>
      </linearGradient>
    </defs>
    <path role="img" aria-label="Photos of a technician on a ladder cleaning storefront glass" fill="url(#crew)"
      d="M222 0H700V210H640C600 210 605 180 560 185C520 190 470 180 430 190C380 200 330 200 300 180C270 160 260 120 230 90C215 70 222 40 222 0Z"/>
    <rect x="260" y="0" width="40" height="200" fill="#fff" opacity=".08"/>
    <path role="img" aria-label="Photo of a worker cleaning high windows with an extension pole" fill="url(#pole)"
      d="M430 215C470 200 520 230 560 225C600 220 640 205 660 235C685 270 670 330 640 360C600 395 540 380 500 360C460 340 440 300 430 270Z"/>
    <path role="img" aria-label="Orange squeegee illustration" fill="var(--orange)"
      d="M686 282L700 296L660 382L646 374Z"/>
  </svg>

  <p class="abs headline" style="left:21px;top:39px;width:200px">The "KRV" Startup package is a complete 3 day Window Cleaning System</p>
  <div class="abs price-bar" style="left:3px;top:97px;width:210px;height:27px">
    <small>Includes Training and<br>Equipment for Just</small><strong>$9,995.00</strong>
  </div>
  <p class="abs note" style="left:21px;top:142px">(Training for Up To 2 Team Members)</p>
  <p class="abs lead" style="left:21px;top:190px">HERE IS JUST SOME OF WHAT YOU GET;</p>

  <div class="abs tag tag--green" style="left:21px;top:218px">Hands-on Window Cleaning Training</div>
  <ul class="abs bullets" style="left:130px;top:214px">
    <li>Basic Hands on Window Cleaning Training</li>
    <li>Ladder Safety Training Techniques</li>
    <li>Bidding &amp; Estimating Techniques</li>
  </ul>

  <div class="abs tag tag--grey" style="left:21px;top:270px">Equipment Includes</div>
  <ul class="abs bullets" style="left:130px;top:269px">
    <li>1 Complete Window Cleaning Bucket &amp; Tool Setup</li>
    <li>4 1/2 Piece Sectional Window Cleaning Ladder Set</li>
  </ul>

  <div class="abs tag tag--green" style="left:21px;top:328px">Company Branding Includes</div>
  <ul class="abs bullets" style="left:130px;top:300px">
    <li>3 Page Website with 3 Months Free Hosting</li>
    <li>1 Logo Design</li>
    <li>2500 Door Hangers</li>
    <li>2500 Post Cards</li>
    <li>6 Uniform Shirts and Hats with Logo</li>
    <li>2 (12.3" x 11.25") Magnetic Vehicle Signs</li>
    <li>1 Designed Letterhead, Business Card &amp; Brochure</li>
  </ul>

  <div class="abs tag tag--grey" style="left:21px;top:396px">Office Set-up</div>
  <ul class="abs bullets" style="left:130px;top:392px;line-height:11px">
    <li>20 hours of Business Consulting</li>
    <li>Window Cleaning Marketing &amp; Internet<br>&nbsp;&nbsp;&nbsp;Advertising Plan</li>
  </ul>

  <div class="abs" style="left:625px;top:130px">
    <div class="brand"><i></i>Tarvelbrook</div>
    <div class="brand" style="margin-top:6px"><i></i>Dovrant Co.</div>
  </div>

  <p class="abs task" style="left:362px;top:285px">Teaching<br>Glass is<br>Our Task.</p>
  <p class="abs package-title" style="left:393px;top:388px;width:306px">The "KRV"</p>
  <div class="abs package-bar" style="left:393px;top:411px;width:306px;height:28px">WINDOW CLEANING Package</div>

  <div class="abs footer">
    <p class="abs" style="left:28px;top:24px">Marcus Delvane</p>
    <div class="abs contact" style="left:122px;top:11px">
      <svg width="7" height="9" viewBox="0 0 7 9"><path d="M3.5 0A3 3 0 0 0 .5 3C.5 5 3.5 9 3.5 9S6.5 5 6.5 3A3 3 0 0 0 3.5 0Z" fill="#fff"/></svg>
      <span>2180 Cedar Ridge Rd Ste 40<br>Millbrook CA 94012</span>
    </div>
    <div class="abs contact" style="left:122px;top:36px">
      <svg width="8" height="7" viewBox="0 0 8 7"><rect x=".5" y=".5" width="7" height="6" fill="none" stroke="#fff"/><path d="M.5 .5L4 4 7.5 .5" fill="none" stroke="#fff"/></svg>
      <span>info@dovrantco.com</span>
    </div>
    <div class="abs contact" style="left:272px;top:14px">
      <svg width="8" height="8" viewBox="0 0 8 8"><path d="M1 0H3L3.5 2 2.5 3A5 5 0 0 0 5 5.5L6 4.5 8 5V7C8 7.5 7.5 8 7 8 3 8 0 5 0 1 0 .5.5 0 1 0Z" fill="#fff"/></svg>
      <span>877-555-0148</span>
    </div>
    <div class="abs contact" style="left:272px;top:34px">
      <svg width="8" height="8" viewBox="0 0 8 8"><path d="M1 0H3L3.5 2 2.5 3A5 5 0 0 0 5 5.5L6 4.5 8 5V7C8 7.5 7.5 8 7 8 3 8 0 5 0 1 0 .5.5 0 1 0Z" fill="#fff"/></svg>
      <span>877-555-0172</span>
    </div>
    <p class="abs url" style="left:398px;top:27px">www.tarvelbrookpolishinstitute.com</p>
  </div>
</section>

<section class="spread spread--lmt">
  <div class="abs title-bar" style="left:34px;top:42px;width:286px;height:27px">The "LMT" Window Cleaning Package</div>
  <p class="abs task" style="left:200px;top:100px;width:115px;text-align:center">Teaching Glass is<br>Our Task.</p>

  <div class="abs photo-circle" role="img" aria-label="Technician cleaning a window frame" style="left:22px;top:102px;width:142px;height:142px;background:linear-gradient(135deg,#c9d0d6,#6e7680)"></div>
  <div class="abs photo-circle" role="img" aria-label="Ladder set against a red wall" style="left:181px;top:158px;width:142px;height:142px;background:linear-gradient(135deg,#d04a5a,#9c1f33)"></div>
  <div class="abs photo-circle" role="img" aria-label="Worker cleaning mini blinds" style="left:20px;top:278px;width:142px;height:142px;background:linear-gradient(135deg,#8d7a62,#cfcac0)"></div>
  <div class="abs photo-circle" role="img" aria-label="Close-up of cleaned blind slats" style="left:187px;top:324px;width:142px;height:142px;background:linear-gradient(135deg,#a1a7ad,#e4e7ea)"></div>

  <p class="abs site" style="left:16px;top:460px">www.tarvelbrookpolishinstitute.com</p>

  <svg class="abs cloud" viewBox="0 0 336 440" aria-hidden="true">
    <path fill="#fff" d="M20 30C10 10 40 0 60 8C80-4 110 4 130 8C160-2 200 2 230 8C260 0 300 4 315 20C336 30 330 60 326 90C334 130 330 180 326 220C334 270 330 320 326 360C336 400 320 430 290 432C250 440 200 434 160 436C110 440 60 436 30 432C5 428 0 400 6 370C0 320 4 270 6 220C0 170 4 120 6 80C0 60 8 40 20 30Z"/>
  </svg>

  <p class="abs headline" style="left:378px;top:64px;width:300px;text-align:center">The "LMT" Startup package is a complete<br>7 day Window Cleaning System</p>
  <p class="abs note" style="left:378px;top:94px;width:300px;text-align:center;font-size:8px">Includes Training and Equipment for Just <b style="color:var(--green-text);font-family:'Roboto Condensed',sans-serif;font-size:11px">$19,995.00</b></p>
  <p class="abs note" style="left:378px;top:108px;width:300px;text-align:center;font-size:8px">(Training for Up To 3 Team Members)</p>
  <p class="abs lead" style="left:378px;top:133px;width:300px;text-align:center">HERE IS JUST SOME OF WHAT YOU GET;</p>

  <div class="abs tag tag--green" style="left:385px;top:185px">Hands-on Window Cleaning Training</div>
  <ul class="abs bullets" style="left:494px;top:166px;line-height:13px">
    <li>Beginning &amp; Advance Window Cleaning Training</li>
    <li>Power Washing Training</li>
    <li>Mini-Blind Cleaning Training</li>
    <li>Ladder safety Training Techniques</li>
    <li>Bidding &amp; Estimating techniques</li>
  </ul>

  <div class="abs tag tag--grey" style="left:385px;top:262px">Equipment Includes</div>
  <ul class="abs bullets" style="left:494px;top:245px;line-height:13px">
    <li>1 Complete Window Cleaning Bucket &amp; Tool Setup</li>
    <li>4 1/2 Piece Sectional Window Cleaning Ladder Set</li>
    <li>The ShadeWash Kit Mobile Mini-Blind Cleaning System</li>
    <li>3 Quick Connect Water Keys</li>
  </ul>

  <div class="abs tag tag--green" style="left:385px;top:339px">Company Branding Includes</div>
  <ul class="abs bullets" style="left:494px;top:311px">
    <li>4 Page Website with 6 Months Free Hosting</li>
    <li>1 Logo Design</li>
    <li>5000 Door Hangers</li>
    <li>5000 Post Cards</li>
    <li>12 Uniform Shirts and Hats with Logo</li>
    <li>2 (12.3" x 11.25") Magnetic Vehicle Signs</li>
    <li>1 Designed Letterhead, Business Card &amp; Brochure</li>
  </ul>

  <div class="abs tag tag--grey" style="left:385px;top:423px">Office Set-up</div>
  <ul class="abs bullets" style="left:494px;top:405px;line-height:11px">
    <li>Overview of LedgerLine Software Application</li>
    <li>Overview of Forms Needed for Business<br>&nbsp;&nbsp;&nbsp;Operation</li>
    <li>Window Cleaning Marketing &amp;<br>&nbsp;&nbsp;&nbsp;Internet Advertising Plan</li>
  </ul>

  <svg class="abs" style="left:620px;top:410px" width="80" height="86" viewBox="0 0 80 86">
    <path role="img" aria-label="Orange squeegee illustration" fill="var(--orange)" d="M70 0L80 12 26 86 12 80Z"/>
  </svg>
</section>

</body>
</html>
```